Real Estate Agent need For Sale sign for

We need a for sale sign for our team based in Los Angeles, CA. My team name is Corvanta Real Estate Group. Also known as Team Corvanta. We are also under the Dunmore Pryce umbrella. We are a real estate team that enjoys contributing to the world through supporting homeowners and sellers achieve their real estate goals. The final design should communicate trust, integrity, and loyalty.
Need to have our team name on there: Team Corvanta, phone number 323-581-7246, my licensed number BRL #5820614 on there. The size of the sign will be 32X36.
Target Market(s)
Home buyers and sellers.
Industry/Entity Type
Real Estate Agent
Colors
Designer to choose colors to be used in the design.
Look and feel

```html
<!DOCTYPE html>
<html lang="en">
<head>
<meta charset="utf-8">
<title>Corvanta Real Estate Group – For Sale Sign</title>
<link rel="stylesheet" href="https://fonts.googleapis.com/css2?family=Saira:wght@500;600;700;800&display=swap">
<style>
  :root {
    --red: #ec1c24;
    --black: #1e1e1e;
    --silver: #d9d9d9;
    --white: #ffffff;
    --ink: #3a3a3a;
    --backdrop: #ecebe8;
  }
  html, body {
    margin: 0;
    padding: 0;
    width: 1200px;
    height: 2174px;
    overflow: hidden;
    background: var(--backdrop);
    font-family: "Saira", Arial, sans-serif;
  }
  .canvas {
    position: relative;
    width: 1200px;
    height: 2174px;
  }
  .sign {
    position: absolute;
    left: 100px;
    top: 524px;
    width: 1000px;
    height: 1125px;
    background: var(--white);
    box-shadow: 0 10px 30px rgba(0,0,0,0.18);
    overflow: hidden;
  }
  .sign-art {
    position: absolute;
    inset: 0;
  }
  .brand {
    position: absolute;
    left: 0;
    right: 0;
    top: 120px;
    text-align: center;
    color: var(--red);
    font-weight: 800;
  }
  .brand-name {
    display: block;
    font-size: 190px;
    line-height: 0.95;
    letter-spacing: -2px;
  }
  .brand-tagline {
    display: block;
    font-size: 60px;
    line-height: 1.1;
    letter-spacing: 1px;
  }
  .sale-box {
    position: absolute;
    left: 80px;
    width: 840px;
    top: 652px;
    height: 168px;
    box-sizing: border-box;
    border: 3px solid var(--white);
    display: flex;
    align-items: center;
    justify-content: center;
    color: var(--white);
    font-weight: 700;
    font-size: 140px;
    letter-spacing: 4px;
    text-shadow: 4px 4px 0 var(--black);
  }
  .phone {
    position: absolute;
    left: 0;
    right: 0;
    top: 838px;
    display: flex;
    align-items: center;
    justify-content: center;
    gap: 22px;
    color: var(--white);
    font-weight: 700;
    font-size: 92px;
    line-height: 1;
  }
  .phone-icon {
    width: 66px;
    height: 66px;
  }
  .footer {
    position: absolute;
    left: 0;
    right: 0;
    top: 990px;
    height: 135px;
    display: flex;
    align-items: center;
    justify-content: space-between;
    padding: 0 46px 0 40px;
    box-sizing: border-box;
  }
  .broker-name {
    color: var(--red);
    font-weight: 600;
    font-size: 40px;
    letter-spacing: 0.5px;
  }
  .license {
    font-size: 31px;
    font-weight: 600;
    color: var(--ink);
  }
  .license-number {
    color: var(--red);
    margin-left: 6px;
  }
</style>
</head>
<body>
<div class="canvas">
  <div class="sign">
    <svg class="sign-art" viewBox="0 0 1000 1125" width="1000" height="1125" aria-hidden="true">
      <path d="M0 545 Q500 385 1000 545 L1000 640 Q500 470 0 640 Z" fill="var(--black)"/>
      <path d="M0 630 Q500 448 1000 620" fill="none" stroke="var(--silver)" stroke-width="10"/>
      <path d="M0 660 Q500 462 1000 660 L1000 990 L0 990 Z" fill="var(--red)"/>
    </svg>

    <div class="brand">
      <span class="brand-name">Corvanta</span>
      <span class="brand-tagline">REAL ESTATE GROUP</span>
    </div>

    <div class="sale-box">FOR SALE</div>

    <div class="phone">
      <svg class="phone-icon" viewBox="0 0 24 24" aria-hidden="true">
        <path fill="var(--white)" d="M6.6 10.8a15.2 15.2 0 0 0 6.6 6.6l2.2-2.2a1 1 0 0 1 1-.25 11.4 11.4 0 0 0 3.6.57 1 1 0 0 1 1 1V20a1 1 0 0 1-1 1A17 17 0 0 1 3 4a1 1 0 0 1 1-1h3.5a1 1 0 0 1 1 1c0 1.25.2 2.45.57 3.57a1 1 0 0 1-.25 1z"/>
        <path fill="none" stroke="var(--white)" stroke-width="1.6" stroke-linecap="round" d="M14 6.5a4 4 0 0 1 3.5 3.5M14.5 2.8a7.5 7.5 0 0 1 6.7 6.7"/>
      </svg>
      <span class="phone-number">323-581-7246</span>
    </div>

    <div class="footer">
      <span class="broker-name">Dunmore Pryce</span>
      <span class="license">Licensed Number<span class="license-number">BRL #5820614</span></span>
    </div>
  </div>
</div>
</body>
</html>
```